Business Card + Letterhead Design for BELMARSH IMPORTS INC.

We already have a logo; now we need a business card + letterhead. We import and distribute flags and souvenirs with an emphasis on soccer related memorabilia. We target various ethnic markets and sporting goods stores. "Wandering Keepsakes"

```html
<!DOCTYPE html>
<html lang="en">
<head>
<meta charset="utf-8">
<title>Belmarsh Imports Inc. — Business Card</title>
<link rel="stylesheet" href="https://fonts.googleapis.com/css2?family=Michroma&display=swap">
<style>
  :root {
    --backdrop: #4a4a4c;
    --card-white: #ffffff;
    --brand-red: #8e1a1c;
    --ink-black: #141414;
    --ink-grey: #8a8a8a;
    --steel-light: #8c8c8c;
    --steel-dark: #2c2c2c;
  }
  html, body {
    margin: 0;
    padding: 0;
    width: 1200px;
    height: 871px;
    overflow: hidden;
    background: var(--backdrop);
    font-family: "Michroma", sans-serif;
  }
  .canvas {
    position: relative;
    width: 1200px;
    height: 871px;
  }
  .card {
    position: absolute;
    left: 285px;
    width: 630px;
    height: 360px;
    box-shadow: 0 10px 30px rgba(0,0,0,0.45);
    overflow: hidden;
  }
  .card-front { top: 45px; }
  .card-back { top: 466px; }
  .card svg { display: block; }
  .brand-name { fill: var(--brand-red); font-family: "Michroma", sans-serif; }
  .contact-title { fill: var(--ink-grey); font-family: "Michroma", sans-serif; font-size: 14px; }
  .contact-line { fill: var(--ink-grey); font-family: "Michroma", sans-serif; font-size: 11px; letter-spacing: 0.5px; }
</style>
</head>
<body>
<main class="canvas">

  <section class="card card-front" aria-label="Business card front">
    <svg width="630" height="360" viewBox="0 0 630 360">
      <rect class="front-paper" x="0" y="0" width="630" height="360" fill="var(--card-white)"/>
      <rect class="front-red-band" x="405" y="0" width="225" height="360" fill="var(--brand-red)"/>

      <g class="front-brand">
        <circle cx="52" cy="66" r="16" fill="var(--brand-red)"/>
        <text class="brand-name" x="80" y="62" font-size="20">BELMARSH</text>
        <text class="brand-name" x="80" y="86" font-size="20">IMPORTS</text>
      </g>

      <g class="front-contact">
        <text class="contact-title" x="36" y="160">BELMARSH IMPORTS INC.</text>
        <text class="contact-line" x="36" y="200">PHONE: (555) 318-2957</text>
        <text class="contact-line" x="36" y="228">FAX: (555) 862-1730</text>
        <text class="contact-line" x="36" y="256">EMAIL: SALES@BELMARSH.COM</text>
        <text class="contact-line" x="36" y="284">WEB: WWW.BELMARSH.COM</text>
      </g>
    </svg>
  </section>

  <section class="card card-back" aria-label="Business card back">
    <svg width="630" height="360" viewBox="0 0 630 360">
      <defs>
        <radialGradient id="steelGlow" cx="0.5" cy="0.35" r="0.75">
          <stop offset="0" stop-color="var(--steel-light)"/>
          <stop offset="1" stop-color="var(--steel-dark)"/>
        </radialGradient>
      </defs>
      <rect class="back-steel" x="0" y="0" width="630" height="360" fill="url(#steelGlow)"/>
      <ellipse class="back-left-arc" cx="-10" cy="190" rx="100" ry="190" fill="var(--ink-black)"/>
      <ellipse class="back-right-arc" cx="640" cy="170" rx="100" ry="190" fill="var(--brand-red)"/>

      <g class="back-brand">
        <circle cx="315" cy="110" r="22" fill="var(--brand-red)"/>
        <text class="brand-name" x="315" y="215" font-size="44" text-anchor="middle">BELMARSH</text>
        <text class="brand-name" x="315" y="265" font-size="26" text-anchor="middle" letter-spacing="12">IMPORTS</text>
      </g>
    </svg>
  </section>

</main>
</body>
</html>
```